Broschüre über Mikro-Mobilitätslösungen vom E-Scooter
Zielgruppe
Wir entwickeln und vermarkten Mikro-Mobilitätslösungen vom E-Scooter bis hin zu stationsgebundenen Verleihsystemen. Kunden sind meist Privatleute aber auch Unternehmen, Hotels oder Kommunen. Wir möchten uns und unsere Produkte in einer Broschüre als Story vorstellen und den Leser dazu animieren, sich alles anzusehen. Mit dynamischen QR-Codes soll dann auch auf die Produkte verlinkt werden. Der Text ist nicht final. Möglichst viel davon soll auch optisch dargestelt werden. Dei Anzahl der Seiten der Broschüre spielt zunächt keine Rolle.
Zu jeder Produktvorstellung sollen auchd ie Technischen Daten aufgeführt werden.
Aufgabenstellung
Frisch, einladend, innovativ Broschüre im Format DIN A 5 quer

```html
<!DOCTYPE html>
<html lang="de">
<head>
<meta charset="utf-8">
<title>Wegfalke – Qualität und Sicherheit</title>
<link rel="stylesheet" href="https://fonts.googleapis.com/css2?family=Bebas+Neue&family=Raleway:wght@400;500&display=swap">
<style>
  :root {
    --bg: #d3d3d3;
    --paper: #efefef;
    --paper-light: #f5f5ee;
    --green: #78b00f;
    --ink: #3e3b39;
    --text: #2f2f2f;
    --sky: #3e78c8;
    --hull: #26345a;
    --pavement: #a9a49d;
  }
  html, body {
    margin: 0;
    width: 1200px;
    height: 1089px;
    overflow: hidden;
    background: var(--bg);
  }
  .spread {
    position: absolute;
    left: 40px;
    top: 334px;
    width: 1120px;
    height: 421px;
    display: flex;
    box-shadow: 0 18px 40px rgba(0,0,0,0.18);
  }
  .page {
    position: relative;
    width: 560px;
    height: 421px;
    overflow: hidden;
  }
  .page-left { background: var(--paper); }
  .page-left .diagonal {
    position: absolute;
    inset: 0;
    width: 100%;
    height: 100%;
  }
  .accent-band {
    position: absolute;
    left: 15px;
    top: 0;
    width: 28px;
    height: 100%;
    background: var(--green);
  }
  .section-label {
    position: absolute;
    left: 66px;
    top: 120px;
    writing-mode: vertical-rl;
    font-family: "Raleway", sans-serif;
    font-size: 6.5px;
    letter-spacing: 2.4px;
    color: var(--green);
    white-space: nowrap;
  }
  .headline {
    position: absolute;
    left: 118px;
    top: 42px;
    margin: 0;
    font-family: "Bebas Neue", sans-serif;
    font-weight: 400;
    font-size: 54px;
    line-height: 51px;
    color: var(--ink);
  }
  .headline-rule {
    position: absolute;
    left: 123px;
    top: 152px;
    width: 43px;
    height: 7px;
    background: var(--ink);
  }
  .body-copy {
    position: absolute;
    left: 123px;
    top: 182px;
    width: 284px;
    font-family: "Raleway", sans-serif;
    font-size: 9.3px;
    line-height: 12px;
    letter-spacing: 0.35px;
    color: var(--text);
  }
  .body-copy p { margin: 0 0 12px; }
  .folio {
    position: absolute;
    bottom: 6px;
    font-family: "Raleway", sans-serif;
    font-size: 8px;
    color: var(--text);
  }
  .page-left .folio { left: 272px; }
  .page-right .folio { left: 278px; color: rgba(255,255,255,0.55); }
  .photo {
    position: absolute;
    inset: 0;
    background:
      linear-gradient(180deg, rgba(0,0,0,0) 55%, var(--pavement) 70%, #8f8a83 100%),
      linear-gradient(90deg, var(--sky) 0%, #5a86c4 18%, #c9c3b6 22%, var(--hull) 32%, #2a3a62 100%);
  }
  .corner-accent {
    position: absolute;
    inset: 0;
    width: 100%;
    height: 100%;
  }
</style>
</head>
<body>
  <main class="spread">
    <section class="page page-left">
      <svg class="diagonal" viewBox="0 0 560 421" preserveAspectRatio="none" aria-hidden="true">
        <polygon points="312,0 560,0 560,421 536,421" fill="var(--paper-light)"/>
      </svg>
      <div class="accent-band"></div>
      <div class="section-label">WEGFALKE - WER WIR SIND</div>
      <h1 class="headline">Qualität und<br>Sicherheit!</h1>
      <div class="headline-rule"></div>
      <div class="body-copy">
        <p>Bei WEGFALKE legen wir großen Wert auf Qualität und Sicherheit. Unsere E-Scooter sind nicht nur robust und langlebig, sondern auch mit modernsten Sicherheitsmerkmalen ausgestattet, um Dir ein sicheres und angenehmes Fahrerlebnis zu bieten. Außerdem bieten wir erstklassigen Kundenservice und wir stehen Dir jederzeit zur Verfügung, um Deine Fragen zu beantworten und Dich bei der Auswahl des perfekten E-Scooters zu unterstützen.</p>
        <p>Wir sind stolz darauf, eine wachsende Gemeinschaft von zufriedenen Kunden zu haben, die unsere E-Scooter schätzen und täglich nutzen, um zur Arbeit zu pendeln, Einkäufe zu erledigen oder einfach die Stadt zu erkunden. Erlebe mit uns eine neue, effizientere und unterhaltsamere Art, sich fortzubewegen!</p>
      </div>
      <div class="folio">03</div>
    </section>
    <section class="page page-right">
      <div class="photo" role="img" aria-label="Foto: fünf Teammitglieder mit Helmen und Jacken stehen mit E-Scootern auf einem gepflasterten Kai vor einem großen dunkelblauen Kreuzfahrtschiff bei blauem Himmel"></div>
      <svg class="corner-accent" viewBox="0 0 560 421" preserveAspectRatio="none" aria-hidden="true">
        <polygon points="402,421 560,284 560,296 416,421" fill="#ffffff" opacity="0.85"/>
        <polygon points="420,421 560,300 560,421" fill="var(--green)"/>
      </svg>
      <div class="folio">04</div>
    </section>
  </main>
</body>
</html>
```